ALL TEXT GRAPHICS TM May 2025 for Instagram

We are looking for a series of social media graphics for Instagram (new size: 4:5 (1080 x 1350 pixels) ratio that are ALL TEXT. We want the following quotes below on each graphic; one quote per graphic. AND, In very small letters at the bottom of each graphic, add @TovaMarshOnline
The look and feel of these graphics should be complimentary to the color palette attached below; but keep them simple. But the design is up to you; at the end of this document, I provided various samples of all text graphics that I like as examples.
Target Market(s)
women looking to lose weight
Look and feel

```html
<!DOCTYPE html>
<html lang="en">
<head>
<meta charset="utf-8">
<title>All Text Graphics · TM · May 2025</title>
<link rel="stylesheet" href="https://fonts.googleapis.com/css2?family=Montserrat:wght@300;400;900&display=swap">
<style>
  :root {
    --canvas: #e0e0e0;
    --blush: #ff9dcb;
    --berry: #cc0066;
    --white: #ffffff;
    --hot: #ff0080;
    --petal: #ffcde6;
    --soft-text: #ffd1e8;
    --chevron-light: #ffb3d9;
  }
  * { margin: 0; padding: 0; box-sizing: border-box; }
  html, body {
    width: 1200px; height: 800px; overflow: hidden;
    background: var(--canvas);
    font-family: "Montserrat", sans-serif;
  }
  .grid { position: relative; width: 1200px; height: 800px; }
  .post {
    position: absolute; width: 207px; height: 258px;
    padding: 0 18px; white-space: nowrap;
  }
  .row-1 { top: 135px; }
  .row-2 { top: 407px; }
  .col-1 { left: 55px; } .col-2 { left: 278px; } .col-3 { left: 499px; }
  .col-4 { left: 719px; } .col-5 { left: 939px; }

  .bg-blush { background: var(--blush); color: var(--berry); }
  .bg-berry { background: var(--berry); color: var(--soft-text); }
  .bg-white { background: var(--white); color: var(--berry); }
  .bg-hot   { background: var(--hot); color: var(--soft-text); }
  .bg-petal { background: var(--petal); color: var(--berry); }

  .chevron { position: absolute; top: 21px; left: 18px; width: 11px; height: 12px; }
  .chevron path { fill: none; stroke: var(--chevron-light); stroke-width: 1.4; }
  .bg-hot .chevron path { stroke: var(--white); }
  .bg-berry .chevron path { stroke: var(--petal); }

  .headline {
    margin-top: 45px;
    font-weight: 900; font-size: 16.5px; line-height: 18.5px;
    letter-spacing: 0.1px;
  }
  .copy {
    margin-top: 8px;
    font-weight: 400; font-size: 16px; line-height: 18.5px;
    letter-spacing: 0.3px;
  }
  .copy strong { font-weight: 900; }
  .cta {
    margin-top: 8px;
    font-weight: 900; font-size: 16.5px; line-height: 18.5px;
  }
  .cta.spaced { margin-top: 16px; }
  .handle {
    position: absolute; bottom: 19px; left: 18px;
    font-weight: 900; font-size: 6px; letter-spacing: 0.1px;
  }
  .handle.right { left: auto; right: 18px; }
  .bg-white .handle.faint { color: var(--chevron-light); }
</style>
</head>
<body>
<main class="grid">

  <article class="post row-1 col-1 bg-blush">
    <svg class="chevron" viewBox="0 0 11 12"><path d="M1 1l4 5-4 5M6 1l4 5-4 5"/></svg>
    <h2 class="headline" style="margin-top:44px">Bloating.<br>Muffin top.<br>Puffy waistline.</h2>
    <p class="copy">Your body’s<br>screaming for a<br>different kind of<br>fix.</p>
    <p class="cta">Here it is</p>
    <p class="handle">@TOVAMARSHONLINE</p>
  </article>

  <article class="post row-1 col-2 bg-berry">
    <svg class="chevron" viewBox="0 0 11 12"><path d="M1 1l4 5-4 5M6 1l4 5-4 5"/></svg>
    <h2 class="headline" style="margin-top:50px">This is the secret<br>women over 40</h2>
    <p class="copy" style="margin-top:0">are using to get<br>snatched; without<br>starving.</p>
    <p class="copy">Comment<br><strong>SKINNY</strong> to get<br>the exact plan.</p>
    <p class="handle right">@TOVAMARSHONLINE</p>
  </article>

  <article class="post row-1 col-3 bg-white">
    <svg class="chevron" viewBox="0 0 11 12"><path d="M1 1l4 5-4 5M6 1l4 5-4 5"/></svg>
    <h2 class="headline" style="margin-top:50px">You’re doing all<br>the “right”<br>things, but your<br>belly won’t go<br>down?</h2>
    <p class="copy">Here’s what you<br>haven’t tried</p>
    <p class="handle">@TOVAMARSHONLINE</p>
  </article>

  <article class="post row-1 col-4 bg-hot">
    <svg class="chevron" viewBox="0 0 11 12"><path d="M1 1l4 5-4 5M6 1l4 5-4 5"/></svg>
    <h2 class="headline" style="margin-top:50px">This 90-day plan<br>helped women<br>over 40</h2>
    <p class="copy">slim down, get a<br>tiny waist and feel<br>sexy again.</p>
    <p class="cta">You’re next.</p>
    <p class="handle">@TOVAMARSHONLINE</p>
  </article>

  <article class="post row-1 col-5 bg-petal">
    <svg class="chevron" viewBox="0 0 11 12"><path d="M1 1l4 5-4 5M6 1l4 5-4 5"/></svg>
    <h2 class="headline" style="margin-top:50px">What worked in<br>your 30s won’t<br>work now.</h2>
    <p class="copy" style="margin-top:16px">Here’s what<br>actually does.<br>Drop 30 Pounds<br>in 3 Months</p>
    <p class="handle">@TOVAMARSHONLINE</p>
  </article>

  <article class="post row-2 col-1 bg-berry">
    <svg class="chevron" viewBox="0 0 11 12"><path d="M1 1l4 5-4 5M6 1l4 5-4 5"/></svg>
    <h2 class="headline" style="margin-top:50px">That stubborn<br>weight?</h2>
    <p class="copy">It’s not your fault.<br>Your hormones<br>are to blame and<br>you’re not alone;</p>
    <p class="cta">But there is<br>a fix.</p>
    <p class="handle right">@TOVAMARSHONLINE</p>
  </article>

  <article class="post row-2 col-2 bg-blush">
    <svg class="chevron" viewBox="0 0 11 12"><path d="M1 1l4 5-4 5M6 1l4 5-4 5"/></svg>
    <h2 class="headline" style="margin-top:50px">Tired. Moody.<br>Stubborn<br>Belly Fat.</h2>
    <p class="copy" style="margin-top:10px">Your hormones<br>are screaming<br>for help!</p>
    <p class="cta">Let’s fix that.</p>
    <p class="handle">@TOVAMARSHONLINE</p>
  </article>

  <article class="post row-2 col-3 bg-hot">
    <svg class="chevron" viewBox="0 0 11 12"><path d="M1 1l4 5-4 5M6 1l4 5-4 5"/></svg>
    <h2 class="headline" style="margin-top:50px">The stubborn<br>belly fat after<br>40?</h2>
    <p class="copy" style="margin-top:10px">It’s not about<br>calories; it’s about<br>your hormones.</p>
    <p class="cta spaced">Here is the fix!</p>
    <p class="handle">@TOVAMARSHONLINE</p>
  </article>

  <article class="post row-2 col-4 bg-petal">
    <svg class="chevron" viewBox="0 0 11 12"><path d="M1 1l4 5-4 5M6 1l4 5-4 5"/></svg>
    <h2 class="headline" style="margin-top:50px">Flat tummy in<br>your 40s?</h2>
    <p class="copy" style="margin-top:10px">It’s still possible!</p>
    <p class="copy">Comment <strong>BYE<br>BELLY</strong> to get the<br>10 secrets to a<br>flatter tummy</p>
    <p class="handle">@TOVAMARSHONLINE</p>
  </article>

  <article class="post row-2 col-5 bg-white">
    <svg class="chevron" viewBox="0 0 11 12"><path d="M1 1l4 5-4 5M6 1l4 5-4 5"/></svg>
    <h2 class="headline" style="margin-top:50px">Your belly<br>isn’t fat…<br>it’s hormonal.</h2>
    <p class="copy" style="margin-top:10px">And here’s how to<br>fix it.&nbsp; Comment<br><strong>HORMONES</strong> if<br>nothing is<br>working.</p>
    <p class="handle faint">@TOVAMARSHONLINE</p>
  </article>

</main>
</body>
</html>
```